Website for Company that serves and supports Investment Banks

We are seeking to have a six page website that provides a basic description of our company's services. Our company provides Financial Models and Investment Memos on an outsourced basis to Small Investment Banks and Investment firms. We do not require a shopping cart. We already have a logo attached.

Target Market(s)

Small, regional investment banks. Small private equity firms.

Industry/Entity Type

Finance And Accounting

Coding

Coded - Design and coding required

Number of Pages Required

5+ page

Requirements
Nice to have
• Please use the logo design to drive how you design the layout for the website

```html
<!DOCTYPE html>
<html lang="en">
<head>
<meta charset="utf-8">
<title>Northfield Analyst</title>
<link href="https://fonts.googleapis.com/css2?family=Poppins:wght@400;500;600&display=swap" rel="stylesheet">
<style>
:root{
  --navy:#0b3e8a;
  --navy-deep:#07306e;
  --ink:#1b1b1b;
  --text:#333;
  --muted:#666;
  --panel:#f2f2f2;
  --panel-line:#e2e2e2;
  --dark:#1f1f1f;
  --white:#fff;
}
*{margin:0;padding:0;box-sizing:border-box}
html,body{width:1200px;height:3586px;overflow:hidden}
body{font-family:"Poppins",sans-serif;color:var(--text);background:var(--white);font-size:12px;line-height:1.75}
section,header,footer{position:relative;width:1200px}
.btn{display:inline-block;background:var(--navy);color:var(--white);font-size:12px;font-weight:500;border-radius:24px;padding:10px 28px;line-height:1.4}
.btn-outline{background:transparent;border:2px solid var(--white);padding:8px 28px}
h2{font-size:25px;font-weight:500;color:var(--ink);line-height:1.2}
.bullets{list-style:none}
.bullets li{position:relative;padding-left:26px;margin-bottom:14px}
.bullets li::before{content:"";position:absolute;left:0;top:5px;width:13px;height:13px;border:1.5px solid #444;border-radius:50%}
.bullets li::after{content:"";position:absolute;left:4px;top:9.5px;width:4px;height:4px;border-right:1.5px solid #444;border-top:1.5px solid #444;transform:rotate(45deg)}

/* header */
.site-header{height:100px}
.brand{position:absolute;left:160px;top:14px;text-align:center;width:200px}
.brand-mark{display:block;width:26px;height:26px;border-radius:50%;background:var(--navy);margin:0 auto 4px}
.brand-name{font-size:15px;font-weight:600;color:var(--navy);line-height:1.2}
.brand-tag{font-size:8px;color:var(--navy);line-height:1.4}
.call{position:absolute;right:160px;top:16px;font-size:17px;font-weight:600;color:var(--navy);display:flex;align-items:center;gap:8px}
.main-nav{position:absolute;right:160px;top:63px;display:flex;gap:26px;font-size:11px;font-weight:500;color:var(--ink)}

/* hero */
.hero{height:490px;background:linear-gradient(100deg,#3c3e42 0%,#6d6a66 35%,#4a4b4f 70%,#2d2f33 100%)}
.hero-photo{position:absolute;inset:0}
.hero-shade{position:absolute;inset:0;background:rgba(10,12,20,.35)}
.hero-copy{position:absolute;left:0;right:0;top:160px;text-align:center;color:var(--white)}
.hero-copy h1{font-size:38px;font-weight:500;line-height:1.2;margin-bottom:18px}
.hero-copy p{font-size:17px;line-height:1.5;width:640px;margin:0 auto}
.arrow{position:absolute;top:228px;width:34px;height:34px;border:1.5px solid rgba(255,255,255,.8);border-radius:50%}
.arrow svg{display:block;margin:10px auto}
.arrow-left{left:36px}.arrow-right{right:36px}

/* about */
.about{height:472px}
.about h2{position:absolute;left:160px;top:40px}
.about .bullets{position:absolute;left:164px;top:86px;width:480px;z-index:1;line-height:22px}
.about .bullets li{margin-bottom:9px}
.about .bullets li::before{top:4px}
.about .bullets li::after{top:8.5px}
.about .btn{position:absolute;left:162px;top:392px}
.about-art{position:absolute;left:690px;top:80px;width:340px;height:270px;background:radial-gradient(ellipse at 55% 55%,#cfe0f5 0%,#eaf2fb 55%,#fff 80%)}

/* leadership */
.leadership{height:536px;background:linear-gradient(180deg,var(--navy) 0%,var(--navy-deep) 100%);color:var(--white);text-align:center}
.leadership h2{color:var(--white);position:absolute;left:0;right:0;top:42px}
.team{position:absolute;left:150px;top:112px;width:900px;display:flex;justify-content:space-between}
.member{width:210px}
.member-photo{width:140px;height:140px;border-radius:50%;border:4px solid var(--white);background:linear-gradient(160deg,#c7c7c7,#8d8d8d);margin:0 auto 14px}
.member-name{font-size:13px;font-weight:500;line-height:1.3}
.member-role{font-size:10px;margin-bottom:10px}
.member-bio{font-size:10.5px;line-height:1.65;height:88px}
.member .btn{margin-top:46px}

/* products */
.products{height:552px}
.products h2{position:absolute;left:0;right:0;top:40px;text-align:center}
.price-card{position:absolute;top:102px;width:423px;height:440px;background:var(--panel);border:1px solid var(--panel-line);padding:20px 26px}
.card-left{left:172px}.card-right{left:612px}
.price-card h3{font-size:13px;font-weight:600;color:var(--navy);margin-bottom:16px}
.price-card h4{font-size:13px;font-weight:500;color:var(--ink);margin-top:10px;margin-bottom:4px}
.price-row{display:flex;justify-content:space-between;font-size:10.5px;line-height:1.95;padding-right:40px}
.price-card .btn{position:absolute;left:26px;bottom:40px}

/* why hire */
.why{height:456px;background:linear-gradient(90deg,#f5f5f5 0%,#f5f5f5 50%,#e6e9ee 100%)}
.why-photo{position:absolute;right:0;top:0;width:560px;height:456px;background:linear-gradient(90deg,rgba(245,245,245,1) 0%,rgba(160,172,190,.7) 35%,#6b7a90 70%,#8ea2bb 100%)}
.why h2{position:absolute;left:160px;top:48px}
.why .bullets{position:absolute;left:164px;top:104px;width:560px}
.why .btn{position:absolute;left:162px;top:368px}

/* process */
.process{height:484px}
.process-art{position:absolute;left:150px;top:86px;width:400px;height:300px;background:radial-gradient(ellipse at 50% 55%,#dfe8f4 0%,#f1f5fa 55%,#fff 80%)}
.process h2{position:absolute;left:552px;top:54px}
.process .bullets{position:absolute;left:552px;top:110px;width:500px}
.process .btn{position:absolute;left:552px;top:386px}

/* contact */
.contact{height:350px;background:var(--dark);color:var(--white)}
.contact-map{position:absolute;inset:0;background:linear-gradient(135deg,#242424,#1b1b1b)}
.contact h2{position:absolute;left:160px;top:56px;color:var(--white);font-size:20px}
.contact-list{position:absolute;left:160px;top:106px;list-style:none;font-size:11px}
.contact-list li{display:flex;gap:14px;margin-bottom:20px;line-height:1.9}
.c-icon{flex:none;width:30px;height:30px;border-radius:50%;background:var(--navy);border:2px solid var(--white);display:flex;align-items:center;justify-content:center}
.map-pin{position:absolute;left:862px;top:92px}

/* footer */
.site-footer{height:146px;background:var(--navy);color:var(--white);text-align:center}
.foot-nav{display:flex;justify-content:center;gap:24px;font-size:11px;font-weight:500;padding-top:34px}
.legal{font-size:10.5px;margin-top:8px}
.social{display:flex;justify-content:center;gap:8px;margin-top:12px}
.social span{width:24px;height:24px;border:1.5px solid var(--white);border-radius:50%}
</style>
</head>
<body>

<header class="site-header">
  <div class="brand">
    <span class="brand-mark"></span>
    <div class="brand-name">NORTHFIELDANALYST.COM</div>
    <div class="brand-tag">Outsourced Financial Analyst Partners</div>
  </div>
  <div class="call">
    <svg width="16" height="16" viewBox="0 0 24 24"><path fill="#0b3e8a" d="M6.6 10.8a15.1 15.1 0 0 0 6.6 6.6l2.2-2.2c.3-.3.7-.4 1-.2 1.1.4 2.3.6 3.6.6.6 0 1 .4 1 1V20c0 .6-.4 1-1 1A17 17 0 0 1 3 4c0-.6.4-1 1-1h3.5c.6 0 1 .4 1 1 0 1.3.2 2.5.6 3.6.1.3 0 .7-.2 1z"/></svg>
    Call Us: 555-010-4821
  </div>
  <nav class="main-nav">
    <span>ABOUT US</span><span>COMPANY LEADERSHIP</span><span>PRODUCT OFFERING</span><span>WHY HIRE?</span><span>PROCESS</span><span>CONTACT</span>
  </nav>
</header>

<section class="hero">
  <div class="hero-photo" role="img" aria-label="Analyst working at a laptop with financial charts on the desk"></div>
  <div class="hero-shade"></div>
  <div class="hero-copy">
    <h1>Northfield Analyst</h1>
    <p>Our company provides Financial Models and Investment Memos on an outsourced basis to Small Investment Banks and Investment firms.</p>
  </div>
  <div class="arrow arrow-left"><svg width="10" height="12" viewBox="0 0 10 12"><path d="M7 1 2 6l5 5" stroke="#fff" stroke-width="1.6" fill="none"/></svg></div>
  <div class="arrow arrow-right"><svg width="10" height="12" viewBox="0 0 10 12"><path d="M3 1l5 5-5 5" stroke="#fff" stroke-width="1.6" fill="none"/></svg></div>
</section>

<section class="about">
  <h2>ABOUT US</h2>
  <div class="about-art" role="img" aria-label="Tablet showing blue financial bar and line charts"></div>
  <ul class="bullets">
    <li>NorthfieldAnalyst.com functions as an outsourced Financial Analyst partner for smaller, regional investment banks, private equity firms, business brokers, and mezzanine loan funds.</li>
    <li>We focus exclusively on lower middle-market clients.</li>
    <li>We believe Financial Models and Investment Memos are two of the most important deal support tools for executing private equity and investment banking transactions.</li>
    <li>NorthfieldAnalyst.com specializes in delivering robust LBO, Growth Equity, Recap and Merger models.</li>
    <li>NorthfieldAnalyst.com specializes in delivering high quality Investment Memos and Investor Powerpoint Presentations.</li>
  </ul>
  <span class="btn">Read More</span>
</section>

<section class="leadership">
  <h2>COMPANY LEADERSHIP</h2>
  <div class="team">
    <div class="member">
      <div class="member-photo" role="img" aria-label="Portrait of Daniel Reyes"></div>
      <div class="member-name">Daniel Reyes</div>
      <div class="member-role">(Managing Partner)</div>
      <p class="member-bio">He has over 12 years of experience producing financial models and drafting investment memos. He previously worked as an investment banking Financial Analyst in Granite Hill Capital.</p>
      <span class="btn btn-outline">Read More</span>
    </div>
    <div class="member">
      <div class="member-photo" role="img" aria-label="Portrait of Owen Hart"></div>
      <div class="member-name">Owen Hart</div>
      <div class="member-role">(Managing Partner)</div>
      <p class="member-bio">He has over 15 years of experience delivering high quality financial models in the investment banking, private equity and corporate finance sectors. Owen Hart previously worked.</p>
      <span class="btn btn-outline">Read More</span>
    </div>
    <div class="member">
      <div class="member-photo" role="img" aria-label="Portrait of Leo Park"></div>
      <div class="member-name">Leo Park</div>
      <div class="member-role">(Vice President)</div>
      <p class="member-bio">He previously worked as a Financial Analyst for a Texas-based middle market private equity firm where he generated valuation, buyout and merger models for deal execution. Leo Park also.</p>
      <span class="btn btn-outline">Read More</span>
    </div>
    <div class="member">
      <div class="member-photo" role="img" aria-label="Portrait of Sam Ellis"></div>
      <div class="member-name">Sam Ellis serves</div>
      <div class="member-role">(Director of Operations)</div>
      <p class="member-bio">He has more than ten years of hands on operational and administrative managerial experience. Sam previously worked as Director of Operations and Marketing Coordinator</p>
      <span class="btn btn-outline">Read More</span>
    </div>
  </div>
</section>

<section class="products">
  <h2>PRODUCT OFFERING</h2>
  <div class="price-card card-left">
    <h3>FINANCIAL MODELS:</h3>
    <h4>Deal Transaction Models:</h4>
    <div class="price-row"><span>LBO, Growth Equity, Recap</span><span>$3,500</span></div>
    <h4 style="margin-top:22px">Valuation Models:</h4>
    <div class="price-row"><span>Discounted Cashflow</span><span>$2,500</span></div>
    <div class="price-row"><span>Comparable Company Analysis</span><span>$1,000</span></div>
    <div class="price-row"><span>Private Multiple Analysis</span><span>$1,000</span></div>
    <span class="btn">Buy Now</span>
  </div>
  <div class="price-card card-right">
    <h3>INVESTMENT DOCUMENTS:</h3>
    <h4>Investment Memos:</h4>
    <div class="price-row"><span>15-20 page Investment Memo</span><span>$3,500</span></div>
    <div class="price-row"><span>15-20 page Investor Powerpoint</span><span>$3,500</span></div>
    <div class="price-row"><span>40-50 page CIM</span><span>$8,500</span></div>
    <h4 style="margin-top:16px">Deal Support Memos:</h4>
    <div class="price-row"><span>2 Executive Summary Teaser Document</span><span>$500</span></div>
    <div class="price-row"><span>2 Page Investment Screening Memo</span><span>$500</span></div>
    <div class="price-row"><span>Customized Industry Research</span><span>$500</span></div>
    <div class="price-row"><span>Customized Company Research</span><span>$500</span></div>
    <span class="btn">Buy Now</span>
  </div>
</section>

<section class="why">
  <div class="why-photo" role="img" aria-label="Businessman in a suit holding a tablet in front of a city skyline"></div>
  <h2>Why Hire NorthfieldAnalyst.com?</h2>
  <ul class="bullets">
    <li>We are much more cost-effective than hiring full-time Analyst pool</li>
    <li>We give You the ability to purchase Financial Models and Investment Memos on a "product-by-product" on demand basis with standardized prices</li>
    <li>Cost of our Financial Models and Investment Memos is less expensive than other outsourced deal providers including Investment bankers, attorneys, accountants and Industry consultants</li>
    <li>Cost of our Financial Models and Investment Memos is less expensive than Quality of Earnings Analysis reports provided by accounting firms</li>
  </ul>
  <span class="btn">Read More</span>
</section>

<section class="process">
  <div class="process-art" role="img" aria-label="Desktop, laptop, tablet and phone showing financial dashboards"></div>
  <h2>How Our Client Intake Process Works?</h2>
  <ul class="bullets">
    <li>Call or email us a brief two sentence description of your deal project and indicate whether you are interested in our Financial Model or Investment Memo products.</li>
    <li>An NorthfieldAnalyst.com client service rep will contact you within 24 hours.</li>
    <li>To ensure confidentiality, we will request that you forward a copy of your Non-Disclosure Agreement for our execution.</li>
    <li>In order for us to get our arms around the transaction we will email you a blank Sources &amp; Uses of Funds template. We will request that you populate this template with all necessary "Flow-of-Funds" information for your transaction.</li>
  </ul>
  <span class="btn">Read More</span>
</section>

<section class="contact">
  <div class="contact-map" role="img" aria-label="Dark street map of the office area"></div>
  <h2>CONTACT US</h2>
  <ul class="contact-list">
    <li><span class="c-icon"><svg width="12" height="14" viewBox="0 0 12 14"><path d="M6 0a5 5 0 0 0-5 5c0 4 5 9 5 9s5-5 5-9a5 5 0 0 0-5-5zm0 7a2 2 0 1 1 0-4 2 2 0 0 1 0 4z" fill="#fff"/></svg></span>
      <span>Address NorthfieldAnalyst.com<br>410 Harbor Street Suite<br>12-204 Lakeview, MA 02100</span></li>
    <li><span class="c-icon"><svg width="12" height="12" viewBox="0 0 24 24"><path fill="#fff" d="M6.6 10.8a15.1 15.1 0 0 0 6.6 6.6l2.2-2.2c.3-.3.7-.4 1-.2 1.1.4 2.3.6 3.6.6.6 0 1 .4 1 1V20c0 .6-.4 1-1 1A17 17 0 0 1 3 4c0-.6.4-1 1-1h3.5c.6 0 1 .4 1 1 0 1.3.2 2.5.6 3.6.1.3 0 .7-.2 1z"/></svg></span>
      <span>Phone: 555-014-2290</span></li>
    <li><span class="c-icon"><svg width="12" height="10" viewBox="0 0 12 10"><rect x="0.5" y="0.5" width="11" height="9" fill="#fff"/><path d="M.5.5 6 5.5 11.5.5" stroke="#0b3e8a" fill="none"/></svg></span>
      <span>Email:info@northfieldanalyst.com</span></li>
  </ul>
  <div class="map-pin c-icon"><svg width="12" height="14" viewBox="0 0 12 14"><path d="M6 0a5 5 0 0 0-5 5c0 4 5 9 5 9s5-5 5-9a5 5 0 0 0-5-5zm0 7a2 2 0 1 1 0-4 2 2 0 0 1 0 4z" fill="#fff"/></svg></div>
</section>

<footer class="site-footer">
  <nav class="foot-nav">
    <span>ABOUT US</span><span>COMPANY LEADERSHIP</span><span>PRODUCT OFFERING</span><span>WHY HIRE?</span><span>PROCESS</span><span>CONTACT</span>
  </nav>
  <p class="legal">© 2017 Northfieldanalyst. All Rights Reserved | Legal and Privacy Statement</p>
  <div class="social"><span></span><span></span><span></span><span></span><span></span></div>
</footer>

</body>
</html>
```